Brisk Lantern Estates, which offers a selection of prime properties (villas

A website that contains: Idea, benefits, destinations (villas), offers, about us, contact, newsletter, social media, blog, look at the attachment, even if it is in German. The idea is that I can easily add new pages, if necessary, with the design you make. Later on we want to add a reservation system, so you can book your villa through the internet. Besides, there is a concierge service available, which organizes everything for the customer, owner, from villa to restaurant, limo service, ... & benefits and emotions through nice pictures / videos, they should be convinced to invest.

Target Market(s)

Investors (golfer and non-golfer) which have 300'000 to invest in a kind of real-estate investing club

Number of Pages Required

5+ page

Font styles to use
Sans Serif

Requirements
Must have
• It must be for wordpress, must have an exclusive touch, high quality, with nice pictures of golf courses. The Logo is gold so it has to match with gold, the font is segan or segoe semilight or similar, sans serif
Nice to have
• may be as well as the possibility to include videos of the different destinations and houses

```html
<!DOCTYPE html>
<html lang="en">
<head>
<meta charset="utf-8">
<title>Brisk Lantern Estates</title>
<link href="https://fonts.googleapis.com/css2?family=Open+Sans:wght@300;400;600;700;800&family=Oswald:wght@300&display=swap" rel="stylesheet">
<style>
:root{
  --gold:#d4a32e;
  --gold-text:#e0b23a;
  --header-bg:#1b1b1b;
  --page-bg:#121212;
  --panel-bg:rgba(20,20,20,.85);
  --form-bg:rgba(25,25,25,.82);
  --text-light:#bdbdbd;
  --white:#fff;
}
*{margin:0;padding:0;box-sizing:border-box}
html,body{width:1200px;height:1200px;overflow:hidden;background:var(--page-bg);font-family:"Open Sans",sans-serif}
.site{position:relative;width:1200px;height:1200px;overflow:hidden}
.header{position:absolute;left:0;top:0;width:1200px;height:107px;background:linear-gradient(#222,#161616)}
.brand{position:absolute;left:128px;top:14px;width:182px;text-align:center}
.brand-mark{display:block;margin:0 auto 6px}
.brand-name{font-weight:300;font-size:18px;color:var(--gold-text);letter-spacing:.2px}
.nav a{position:absolute;top:43px;font-size:11.5px;font-weight:700;color:#9a9a9a;text-decoration:none;letter-spacing:.3px}
.nav a.active{color:var(--gold)}
.caret{display:inline-block;margin-left:5px;border:3.5px solid transparent;border-top-color:#888;vertical-align:middle;transform:translateY(2px)}
.btn-top{position:absolute;left:805px;top:32px;width:121px;height:35px;background:var(--gold);color:var(--white);font-size:11.5px;font-weight:700;text-align:center;line-height:35px;letter-spacing:.3px}
.social{position:absolute;left:942px;top:32px;display:flex;gap:2px}
.social span{width:37px;height:35px;display:block}
.hero{position:absolute;left:0;top:107px;width:1200px;height:511px;background:linear-gradient(90deg,#6a3a22 0%,#8a5a3a 14%,#6fb6cf 32%,#3ea7c4 48%,#58a1a0 62%,#5d8a3e 78%,#4d7a36 100%)}
.hero-strip{position:absolute;left:0;top:0;width:100%;height:7px;background:#6a6a6a}
.hero-ground{position:absolute;left:0;bottom:0;width:100%;height:230px;background:linear-gradient(180deg,rgba(60,120,40,0) 0%,rgba(70,130,50,.7) 55%,rgba(200,200,190,.55) 100%)}
.pitch{position:absolute;left:0;top:210px;width:214px;height:250px;background:rgba(30,30,30,.55)}
.pitch-inner{position:absolute;left:0;top:210px;width:204px;height:250px;background:var(--panel-bg);overflow:hidden}
.pitch-inner span{position:absolute;white-space:nowrap;color:var(--white)}
.p1{right:149px;top:25px;font-size:14px}
.p2{right:26px;top:40px;font-size:38px;font-weight:800;color:var(--gold-text)!important}
.p3{right:99px;top:93px;font-size:24px;font-weight:800;color:var(--gold-text)!important}
.p4{right:42px;top:125px;font-size:19px;font-weight:800}
.rule{position:absolute;left:0;top:164px;width:178px;height:1px;background:#555}
.p5{right:76px;top:174px;font-size:14px}
.p6{right:106px;top:195px;font-size:30px;font-weight:800}
.form{position:absolute;left:714px;top:139px;width:352px;height:442px;background:var(--form-bg);border-radius:6px 6px 0 0}
.form-head{height:61px;background:#000;border-radius:6px 6px 0 0;color:var(--white);font-weight:700;font-size:17px;text-align:center;line-height:61px}
.form-note{position:absolute;top:70px;width:100%;text-align:center;font-size:11px;color:var(--white)}
.field{position:absolute;left:18px;width:315px;height:47px;border:1px solid #cfcfcf;color:var(--white);font-size:12.5px;line-height:45px;padding-left:20px}
.sel{position:absolute;right:3px;top:3px;width:20px;height:39px;background:#555}
.sel::after{content:"";position:absolute;left:6px;top:15px;width:6px;height:6px;border-right:1.5px solid #ddd;border-bottom:1.5px solid #ddd;transform:rotate(45deg)}
.country{position:absolute;left:66px;top:4px;width:20px;height:39px;background:#555}
.country::after{content:"";position:absolute;left:6px;top:15px;width:6px;height:6px;border-right:1.5px solid #ddd;border-bottom:1.5px solid #ddd;transform:rotate(45deg)}
.phone{position:absolute;left:97px}
.btn-form{position:absolute;left:19px;top:382px;width:313px;height:45px;background:var(--gold);color:var(--white);font-weight:700;font-size:15px;text-align:center;line-height:45px;letter-spacing:.5px}
.band{position:absolute;left:0;top:618px;width:1200px;height:13px;background:#0a0a0a}
.title{position:absolute;left:544px;top:678px;width:105px;text-align:center}
.title hr{border:0;height:1px;background:#555;margin:0 0 4px}
.title h2{font-family:"Oswald",sans-serif;font-weight:300;font-size:36px;color:var(--gold-text);margin:10px -40px 12px;line-height:42px}
.portrait{position:absolute;top:814px;width:192px;height:192px;border-radius:50%;border:2px solid #eee;background:radial-gradient(circle at 50% 40%,#b08a70 0%,#5a4a44 45%,#2a2e3a 100%)}
.idea{position:absolute;left:521px;width:545px;color:var(--text-light);font-weight:300;font-size:18px;line-height:28px}
.idea li{list-style:none;position:relative}
.idea li::before{content:"";position:absolute;left:-20px;top:10px;width:9px;height:9px;border-radius:50%;background:#aaa}
.divider{position:absolute;left:521px;top:942px;width:545px;height:1px;background:#444}
.reasons-head{position:absolute;left:521px;top:972px;width:470px;color:var(--gold-text);font-weight:700;font-size:17.5px;line-height:28px}
.reasons{position:absolute;color:var(--text-light);font-weight:300;font-size:17.5px;list-style:none}
.reasons li{position:relative;height:34px}
.reasons li::before{content:"";position:absolute;left:-17px;top:10px;width:9px;height:9px;border-radius:50%;background:#aaa}
.footer{position:absolute;left:0;top:1190px;width:1200px;height:10px;background:#000}
</style>
</head>
<body>
<div class="site">
  <header class="header">
    <div class="brand">
      <svg class="brand-mark" width="72" width2="" height="44" viewBox="0 0 72 44" aria-hidden="true">
        <rect x="22" y="10" width="28" height="28" fill="none" stroke="#d4a32e" stroke-width="2"/>
      </svg>
      <div class="brand-name">BRISK LANTERN ESTATES</div>
    </div>
    <nav class="nav">
      <a class="active" style="left:342px">HOME</a>
      <a style="left:409px">ABOUT US</a>
      <a style="left:503px">DESTINATIONS<i class="caret"></i></a>
      <a style="left:631px">BENEFITS<i class="caret"></i></a>
      <a style="left:727px">CONTACT</a>
    </nav>
    <div class="btn-top">ENQUIRE NOW</div>
    <div class="social">
      <span style="background:#3b5b99" role="img" aria-label="Social profile one"></span>
      <span style="background:#1e9ae0" role="img" aria-label="Social profile two"></span>
      <span style="background:#d4352a" role="img" aria-label="Video channel"></span>
    </div>
  </header>

  <section class="hero" role="img" aria-label="Beachfront villa veranda with palm trees, sea view and golf course greens">
    <div class="hero-strip"></div>
    <div class="hero-ground"></div>
  </section>

  <div class="pitch"></div>
  <div class="pitch-inner">
    <span class="p1">WE BRING-</span>
    <span class="p2">REAL ESTATE</span>
    <span class="p3">INVESTMENT</span>
    <span class="p4">&amp; LIFESTYLE TOGETHER</span>
    <div class="rule"></div>
    <span class="p5">PRICE STARTING FROM</span>
    <span class="p6">€ 318,000</span>
  </div>

  <form class="form">
    <div class="form-head">Register Your Interest</div>
    <div class="form-note">All fields are compulsory.</div>
    <div class="field" style="top:98px">-Select Title<span class="sel"></span></div>
    <div class="field" style="top:155px">First Name</div>
    <div class="field" style="top:211px">Last Name</div>
    <div class="field" style="top:268px">Email Address</div>
    <div class="field" style="top:323px">India<span class="country"></span><span class="phone">+91 Phone Number</span></div>
    <div class="btn-form">ENQUIRE NOW</div>
  </form>

  <div class="band"></div>

  <div class="title">
    <hr><hr>
    <h2>OUR IDEA</h2>
    <hr><hr>
  </div>

  <div class="portrait" style="left:132px" role="img" aria-label="Portrait of co-founder"></div>
  <div class="portrait" style="left:266px" role="img" aria-label="Portrait of co-founder"></div>

  <ul class="idea" style="top:796px">
    <li>The idea follows a need for holidays, variety and enjoyment at the highest level &amp; at attractive conditions.</li>
  </ul>
  <ul class="idea" style="top:867px">
    <li>The concept is based on many discussions and has been developed with the help of various experts from various fields</li>
  </ul>
  <div class="divider"></div>
  <p class="reasons-head">Real estate in golf resorts are appreciated by golfers as non-golfers: The reasons are:</p>
  <ul class="reasons" style="left:534px;top:1033px">
    <li>Quiet</li>
    <li>Resort Infrastructure &amp; Services</li>
  </ul>
  <ul class="reasons" style="left:824px;top:1033px">
    <li>Well maintained park landscape</li>
    <li>Worth preserving</li>
  </ul>

  <footer class="footer"></footer>
</div>
</body>
</html>
```